Agricultural and Earthmoving business card design

We need a business card design for a new company based in Kilmore, Victoria. We are a versatile company with two specialties, the first is an earthworks side, we do big and small jobs, from soccer fields for councils and football clubs down to house cuts for the public, horse ridding arena's, tennis courts and drainage are also small jobs we have experience in. Not only do we do earthmoving, but we also have a lot of experience in the agricultural side of machinery work, from pasture improvements to a lot of experience in hay contracting. We need a business card that doesn't focus on only one side of our business but blends both skills. We would like a primarily black business card that incorporates our company logo. Our company colours are black red , grey and white.

Industry/Entity Type

House

Contact Information for Business Card

Marwick Contracting, Dale Marwick, 2741 Ferngate Rd Brackenvale Vic 3769, Phone: 03 5926 4083, Mobile: 0437 902 618. Specialising in Earthmoving, synthetic and natural turf, landscaping, drainage. Also specialising in Agricultural improvements and hay contracting.

Requirements
Must have
• A good blend of both earthmoving and agricultural contracting. Company logo.

```html
<!DOCTYPE html>
<html lang="en">
<head>
<meta charset="utf-8">
<title>Marwick Contracting – Business Card</title>
<link rel="stylesheet" href="https://fonts.googleapis.com/css2?family=Arimo:wght@400;700&family=Open+Sans:wght@600;700&display=swap">
<style>
  :root {
    --sky: #c9d3d6;
    --mist: #f4f1ee;
    --sunset: #f79a4a;
    --frame-red: #e2191c;
    --panel: #1f1f20;
    --title-grey: #d6dadb;
    --text-light: #e4e6e6;
    --text-soft: #d2d6d6;
    --white: #ffffff;
    --logo-grey: #8a8683;
  }
  html, body {
    margin: 0;
    padding: 0;
    overflow: hidden;
  }
  .card {
    position: relative;
    width: 1200px;
    height: 741px;
    overflow: hidden;
    background: linear-gradient(180deg, var(--sky) 0%, var(--mist) 42%, var(--sunset) 100%);
    font-family: "Arimo", Arial, sans-serif;
  }
  .card__frame {
    position: absolute;
    left: 16px;
    top: 16px;
    width: 1162px;
    height: 700px;
    border: 3px solid var(--frame-red);
  }
  .card__panel {
    position: absolute;
    left: 43px;
    top: 43px;
    width: 1114px;
    height: 662px;
    background: var(--panel);
  }
  .brand-mark {
    position: absolute;
    left: 170px;
    top: 116px;
    display: flex;
    align-items: center;
    gap: 14px;
    font-family: "Arimo", Arial, sans-serif;
    font-weight: 700;
    font-size: 34px;
    letter-spacing: 2px;
    color: var(--logo-grey);
  }
  .brand-mark__square {
    width: 34px;
    height: 34px;
    background: var(--logo-grey);
  }
  .company-name {
    position: absolute;
    left: 467px;
    top: 50px;
    margin: 0;
    font-family: "Arimo", Arial, sans-serif;
    font-weight: 700;
    font-size: 65px;
    line-height: 75px;
    font-variant: small-caps;
    letter-spacing: 1px;
    color: var(--title-grey);
    white-space: nowrap;
  }
  .owner-name {
    position: absolute;
    left: 763px;
    top: 124px;
    margin: 0;
    font-family: "Open Sans", sans-serif;
    font-weight: 700;
    font-size: 40px;
    line-height: 54px;
    color: var(--title-grey);
    white-space: nowrap;
  }
  .specialties {
    position: absolute;
    left: 43px;
    width: 1114px;
    top: 230px;
    margin: 0;
    text-align: center;
    font-family: "Open Sans", sans-serif;
    font-weight: 600;
    font-size: 28px;
    line-height: 38px;
    color: var(--text-soft);
    white-space: nowrap;
  }
  .services {
    position: absolute;
    left: 80px;
    top: 357px;
    margin: 0;
    padding: 0 0 0 23px;
    font-size: 26px;
    line-height: 38px;
    color: var(--text-light);
    white-space: nowrap;
  }
  .services strong {
    font-weight: 700;
  }
  .about {
    position: absolute;
    right: 73px;
    top: 350px;
    margin: 0;
    text-align: right;
    font-size: 26px;
    line-height: 38px;
    color: var(--text-light);
    white-space: nowrap;
  }
  .contact {
    position: absolute;
    left: 74px;
    top: 605px;
    margin: 0;
    font-weight: 700;
    font-size: 35px;
    line-height: 44px;
    color: var(--white);
    white-space: nowrap;
  }
  .address {
    position: absolute;
    left: 640px;
    width: 500px;
    top: 603px;
    margin: 0;
    text-align: center;
    font-size: 35px;
    line-height: 42px;
    color: var(--text-soft);
    font-style: normal;
    white-space: nowrap;
  }
</style>
</head>
<body>
  <div class="card">
    <div class="card__frame"></div>
    <div class="card__panel"></div>

    <div class="brand-mark">
      <span class="brand-mark__square"></span>
      <span>MARWICK</span>
    </div>

    <h1 class="company-name">Marwick Contracting</h1>
    <h2 class="owner-name">Dale Marwick</h2>

    <p class="specialties">
      Specialising in Earthmoving, synthetic and natural turf, landscaping &amp; drainage<br>
      Also specialising in Agricultural improvements and hay contracting
    </p>

    <ul class="services">
      <li><strong>BIG</strong> and small jobs</li>
      <li>Soccer fields for councils and football clubs</li>
      <li>House cuts for the public</li>
      <li>Horse riding arenas</li>
      <li>Tennis courts and drainage</li>
    </ul>

    <p class="about">
      Not only do we do earthmoving...<br>
      we also have a lot of experience in<br>
      the agricultural side of machinery work,<br>
      from pasture improvements<br>
      to a lot of experience in hay contracting.
    </p>

    <p class="contact">
      Phone: 03 5926 4083<br>
      Mobile: 0437 902 618
    </p>

    <address class="address">
      Address: 2741 Ferngate Rd<br>
      Brackenvale Vic 3769
    </address>
  </div>
</body>
</html>
```